Relocation/furniture installation company needs new business cards

we are a relocation and furniture installation company mainly dealing with corporate clients and we are looking for new business card ideas. Cards should incorporate our logo and list our website, phone number and services. The company is only 2 years old but with more staff joining we are in the need for more business cards, so something with an awesome design that is eye catching would go a long way to insure we get our name out there and look good to potential new clients.

Target Market(s)

Corporate

Industry/Entity Type

Trade

Contact Information for Business Card

www.mervoline.co.nz
0508 4 bravok

furniture installation
business relocations
joinery installation
commercial property maintenance

Colors
0592cd
34a7d8
85cae6
85acd3
0356a4
cfdfed
cee9f5
757575
474747

Requirements
Must have
• Business relocations and furniture installation specialists
Nice to have
• something that incorporates our logo.

```html
<!DOCTYPE html>
<html lang="en">
<head>
<meta charset="utf-8">
<title>Mervoline business cards</title>
<link href="https://fonts.googleapis.com/css2?family=Lato:wght@400;700;900&display=swap" rel="stylesheet">
<style>
  :root {
    --backdrop: #d9dde3;
    --card: #ffffff;
    --brand-blue: #2a3a99;
    --text-grey: #474747;
    --shadow: rgba(0, 0, 0, 0.18);
  }
  * { margin: 0; padding: 0; box-sizing: border-box; }
  html, body {
    width: 1200px;
    height: 1200px;
    overflow: hidden;
    background: var(--backdrop);
    font-family: "Lato", sans-serif;
  }
  .sheet {
    width: 1200px;
    height: 1200px;
    display: flex;
    flex-direction: column;
    align-items: center;
    justify-content: center;
    gap: 24px;
  }
  .card {
    position: relative;
    width: 960px;
    height: 549px;
    background: var(--card);
    box-shadow: 0 6px 24px var(--shadow);
    overflow: hidden;
  }

  /* front */
  .front__name {
    position: absolute;
    left: 56px;
    top: 48px;
    font-weight: 900;
    font-size: 78px;
    letter-spacing: 10px;
    color: var(--brand-blue);
    line-height: 1;
    display: flex;
    align-items: center;
    gap: 18px;
  }
  .front__name .mark {
    width: 26px;
    height: 26px;
    background: var(--brand-blue);
  }
  .contact {
    position: absolute;
    left: 60px;
    top: 158px;
    font-size: 22px;
    color: var(--text-grey);
    line-height: 1.45;
  }
  .services {
    position: absolute;
    left: 60px;
    top: 262px;
    list-style: none;
    font-size: 22px;
    color: var(--text-grey);
    line-height: 1.5;
  }
  .services li {
    display: flex;
    align-items: center;
    gap: 14px;
  }
  .services svg { width: 16px; height: 16px; flex: none; }
  .front__band {
    position: absolute;
    left: 0;
    bottom: 0;
    width: 960px;
    height: 200px;
  }

  /* back */
  .back {
    display: flex;
    align-items: center;
    justify-content: center;
  }
  .back__name {
    font-weight: 900;
    font-size: 88px;
    letter-spacing: 12px;
    color: var(--brand-blue);
    display: flex;
    align-items: center;
    gap: 22px;
  }
  .back__name .mark {
    width: 30px;
    height: 30px;
    background: var(--brand-blue);
  }
</style>
</head>
<body>
<main class="sheet">

  <section class="card front" aria-label="Business card front">
    <div class="front__name">MERVOLINE<span class="mark"></span></div>
    <div class="contact">
      <p>0508 4 bravok</p>
      <p>www.mervoline.co.nz</p>
    </div>
    <ul class="services">
      <li><svg viewBox="0 0 10 10"><polygon points="5,0 6.2,3.6 10,3.7 7,6 8.1,9.6 5,7.5 1.9,9.6 3,6 0,3.7 3.8,3.6" fill="var(--brand-blue)"/></svg>furniture installation</li>
      <li><svg viewBox="0 0 10 10"><polygon points="5,0 6.2,3.6 10,3.7 7,6 8.1,9.6 5,7.5 1.9,9.6 3,6 0,3.7 3.8,3.6" fill="var(--brand-blue)"/></svg>business relocations</li>
      <li><svg viewBox="0 0 10 10"><polygon points="5,0 6.2,3.6 10,3.7 7,6 8.1,9.6 5,7.5 1.9,9.6 3,6 0,3.7 3.8,3.6" fill="var(--brand-blue)"/></svg>joinery installation</li>
      <li><svg viewBox="0 0 10 10"><polygon points="5,0 6.2,3.6 10,3.7 7,6 8.1,9.6 5,7.5 1.9,9.6 3,6 0,3.7 3.8,3.6" fill="var(--brand-blue)"/></svg>commercial property maintenance</li>
    </ul>
    <svg class="front__band" viewBox="0 0 960 200" preserveAspectRatio="none" aria-hidden="true">
      <polygon points="0,150 440,150 500,90 700,90 700,130 800,160 960,160 960,200 0,200" fill="var(--brand-blue)"/>
    </svg>
  </section>

  <section class="card back" aria-label="Business card back">
    <div class="back__name">MERVOLINE<span class="mark"></span></div>
  </section>

</main>
</body>
</html>
```